Occupational Therapist does home accessibility for disabled folks; needs business card design

We need a business card for a company in Portland, Oregon that specializes in making homes accessible, comfortable, and functional for people who are disabled or aging who would like to stay in THEIR home. Our medical background as Occupational Therapists allows us to translate the functional needs of the person into the recommendations for the design of the home remodel.

Target Market(s)

Elderly, children of elderly
People with disabilities, families of people with disabilities

Industry/Entity Type

Business

Contact Information for Business Card

Company name: HomeWise
Name: Danielle Reyes Crawford, OTR/L, CAPS, ECHM
Occupational Therapist, Home Modification & Accessibility Specialist
website: www.homewiseforyears.com
email: homewiseforyears@nestmail.example
phone: (503)218-4057
CCB #: 487315

Font styles to use
Sans Serif

Requirements
Must have
• My logo
• Easy to read font with contrasting background
• Please list the Services offered: Occupational Therapy, Home safety & accessibility assessments, Home modification consulting, project management
Nice to have
• Friendly, welcoming feel
Should not have
• Dark colored background

```html
<!DOCTYPE html>
<html lang="en">
<head>
<meta charset="utf-8">
<title>HomeWise Business Card</title>
<link rel="stylesheet" href="https://fonts.googleapis.com/css2?family=Open+Sans:wght@400;600;700&display=swap">
<style>
  :root {
    --orange: #d4821c;
    --orange-deep: #b86d12;
    --white: #ffffff;
    --grey-text: #5f5f5f;
    --dark-text: #3d3d3d;
    --stage: #ece8e2;
  }
  * { margin: 0; padding: 0; box-sizing: border-box; }
  html, body { width: 1200px; height: 950px; overflow: hidden; }
  body {
    background: var(--stage);
    font-family: "Open Sans", Arial, sans-serif;
    position: relative;
  }
  .card {
    position: absolute;
    width: 560px;
    height: 320px;
    border-radius: 4px;
    overflow: hidden;
    box-shadow: 0 6px 18px rgba(0,0,0,0.18);
  }
  .brand-square { width: 16px; height: 16px; flex: none; }
  .brand-name { font-weight: 700; line-height: 1; letter-spacing: 0.5px; white-space: nowrap; }

  /* Front */
  .card-front { left: 90px; top: 110px; background: var(--white); }
  .front-band { position: absolute; left: 0; top: 0; width: 560px; height: 320px; }
  .front-brand {
    position: absolute;
    left: 40px; top: 118px;
    display: flex; align-items: center; gap: 12px;
  }
  .front-brand .brand-square { background: var(--orange); }
  .front-brand .brand-name { font-size: 40px; color: var(--orange); }
  .holder { position: absolute; left: 40px; bottom: 26px; }
  .holder-name { color: var(--orange); font-weight: 700; font-size: 21px; line-height: 1.36; }
  .holder-creds { color: var(--orange); font-weight: 700; font-size: 15px; line-height: 1.36; margin-bottom: 6px; }
  .holder-role { color: var(--grey-text); font-size: 14.5px; line-height: 1.35; }
  .contact {
    position: absolute; right: 30px; top: 36px;
    color: var(--dark-text); font-size: 13px; line-height: 1.8;
    list-style: none;
  }
  .contact li { display: flex; justify-content: flex-end; align-items: center; gap: 8px; white-space: nowrap; }
  .contact .icon { width: 14px; height: 14px; flex: none; }
  .contact .spacer { width: 14px; flex: none; }

  /* Back */
  .card-back { left: 550px; top: 520px; background: var(--orange); color: var(--white); }
  .back-brand {
    position: absolute; left: 0; right: 0; top: 64px;
    display: flex; justify-content: center; align-items: center; gap: 14px;
  }
  .back-brand .brand-square { width: 18px; height: 18px; background: var(--white); }
  .back-brand .brand-name { font-size: 56px; color: var(--white); }
  .services { position: absolute; left: 30px; right: 30px; top: 190px; text-align: center; }
  .services-title { font-weight: 700; font-size: 17px; margin-bottom: 8px; }
  .services-list { font-size: 14px; line-height: 1.55; }
</style>
</head>
<body>
  <section class="card card-front" aria-label="Business card front">
    <svg class="front-band" viewBox="0 0 560 320" aria-hidden="true">
      <polygon points="0,0 240,0 0,112" fill="var(--orange)"/>
      <polygon points="240,0 252,0 0,118 0,112" fill="var(--orange-deep)"/>
    </svg>
    <div class="front-brand">
      <span class="brand-square"></span>
      <span class="brand-name">HomeWise</span>
    </div>
    <div class="holder">
      <p class="holder-name">Danielle Reyes Crawford</p>
      <p class="holder-creds">OTR/L, CAPS, ECHM</p>
      <p class="holder-role">Occupational Therapist<br>Home Modification &amp;<br>Accessibility Specialist</p>
    </div>
    <ul class="contact">
      <li>CCB #: 487315<span class="spacer"></span></li>
      <li>(503)218-4057
        <svg class="icon" viewBox="0 0 14 14" aria-hidden="true"><circle cx="7" cy="7" r="7" fill="var(--orange)"/><path d="M4.2 3.6c.4-.4.9-.4 1.2 0l.7 1c.2.3.2.7-.1 1l-.4.4c.4.9 1.1 1.6 2 2l.4-.4c.3-.3.7-.3 1-.1l1 .7c.4.3.4.8 0 1.2l-.5.5c-2.6.3-5.9-3-5.8-5.8z" fill="var(--white)"/></svg></li>
      <li>homewiseforyears@nestmail.example
        <svg class="icon" viewBox="0 0 14 14" aria-hidden="true"><circle cx="7" cy="7" r="7" fill="var(--orange)"/><rect x="3.5" y="4.5" width="7" height="5" fill="none" stroke="var(--white)" stroke-width="1"/><path d="M3.5 4.5 7 7.3l3.5-2.8" fill="none" stroke="var(--white)" stroke-width="1"/></svg></li>
      <li>www.homewiseforyears.com
        <svg class="icon" viewBox="0 0 14 14" aria-hidden="true"><circle cx="7" cy="7" r="7" fill="var(--orange)"/><circle cx="7" cy="7" r="3.8" fill="none" stroke="var(--white)" stroke-width="1"/><path d="M3.2 7h7.6M7 3.2c-1.6 2.2-1.6 5.4 0 7.6M7 3.2c1.6 2.2 1.6 5.4 0 7.6" fill="none" stroke="var(--white)" stroke-width=".8"/></svg></li>
    </ul>
  </section>

  <section class="card card-back" aria-label="Business card back">
    <div class="back-brand">
      <span class="brand-square"></span>
      <span class="brand-name">HomeWise</span>
    </div>
    <div class="services">
      <p class="services-title">Services</p>
      <p class="services-list">Occupational Therapy | Home safety &amp; accessibility assessments<br>Home modification consulting | project management</p>
    </div>
  </section>
</body>
</html>
```